Velmora Diagnostics Website

Project Description – Velmora Website Design
We need a clean, modern, and professional website for Velmora Diagnostics, a Ashgrove Hollis University of Dunmere spin-out focused on early cancer detection. Our first product, GlandSURE™, is a urine-based risk assessment test for pancreatic cancer, supported by strong clinical validation and partnerships with leading hospitals.

The site should:

Communicate trust, innovation, and clinical credibility.
Feature a clear value proposition on the home page with strong calls to action for investors, clinicians, and partners.
Showcase our technology, science, and clinical evidence in a way that is accessible but authoritative.
Highlight our university heritage, team, and collaborators.
Include sections for products/services, news/press, and contact forms.
Be fully responsive, WordPress compatible, SEO-friendly, and WCAG 2.1 AA accessible.

We want a minimalist, elegant design with subtle animations, strong visuals (e.g., science/biotech imagery), and a clear structure for future growth.
Deliverables should include editable design files (Figma/Sketch/Adobe XD) and a style guide.

```html
<!DOCTYPE html>
<html lang="en">
<head>
<meta charset="utf-8">
<title>Velmora Diagnostics – Early Cancer Detection</title>
<link href="https://fonts.googleapis.com/css2?family=Poppins:wght@400;500;600;700&display=swap" rel="stylesheet">
<style>
:root{
  --blue:#3b86d6;
  --sky:#6cc7ee;
  --sky-soft:#b6e2f5;
  --yellow:#f5c634;
  --ink:#1f2430;
  --muted:#5b6170;
  --card:#f3f3f3;
  --white:#ffffff;
  --footer:#e9e9ea;
}
*{box-sizing:border-box;margin:0;padding:0}
html,body{width:1200px;height:3641px;overflow:hidden}
body{position:relative;font-family:'Poppins',sans-serif;color:var(--ink);background:var(--white)}
.abs{position:absolute}
.ph{position:absolute;border-radius:50%}

/* header */
.logo{display:flex;align-items:center;gap:12px;color:var(--blue);font-weight:600;letter-spacing:1px}
.logo-dot{width:30px;height:30px;border-radius:50%;background:var(--yellow)}
.site-logo{left:75px;top:16px;font-size:22px}
.nav{left:458px;top:16px;display:flex;align-items:center;gap:28px;font-size:13px;font-weight:500}
.nav .active{background:var(--blue);color:#fff;width:52px;height:52px;border-radius:50%;display:flex;align-items:center;justify-content:center}
.btn-login{left:937px;top:18px;width:84px;height:40px;border:1.5px solid var(--sky);border-radius:20px;font-size:13px;font-weight:500;display:flex;align-items:center;justify-content:center;gap:6px}
.btn-signup{left:1035px;top:16px;width:90px;height:42px;background:var(--yellow);color:#fff;border-radius:21px;font-size:13px;font-weight:600;display:flex;align-items:center;justify-content:center}

/* hero */
.hero-bg{left:0;top:0;width:1200px;height:560px;background:linear-gradient(100deg,#fff 30%,#eef4fb 100%)}
.eyebrow{left:75px;top:204px;font-size:13px;color:var(--yellow);font-weight:500}
.hero-title{left:73px;top:240px;width:520px;font-size:37px;line-height:39px;font-weight:600;white-space:nowrap}
.hero-text{left:75px;top:378px;width:470px;font-size:12px;line-height:19px;color:var(--muted)}
.btn-learn{left:75px;top:441px;width:127px;height:40px;background:var(--yellow);color:#fff;border-radius:20px;font-size:12px;font-weight:500;display:flex;align-items:center;justify-content:center}
.hero-link{left:228px;top:452px;font-size:12px}
.pill{background:#fff;border-radius:8px;box-shadow:0 6px 20px rgba(40,80,130,.12);display:flex;align-items:center;gap:10px;font-size:12px;font-weight:500}

/* features */
.feature{width:211px;height:142px;top:688px;background:var(--card);border-radius:14px;padding:54px 22px 0}
.feature h3{font-size:15px;font-weight:600;margin-bottom:6px}
.feature p{font-size:11.5px;line-height:19px;color:var(--muted)}
.feature.is-active{background:var(--sky)}
.feature.is-active h3,.feature.is-active p{color:#fff}
.f-icon{position:absolute;top:-35px;left:22px;width:72px;height:72px;border-radius:50%;background:var(--blue);border:4px solid #fff;display:flex;align-items:center;justify-content:center}
.is-active .f-icon{background:var(--yellow)}

/* stats banner */
.stats{left:73px;top:916px;width:1052px;height:162px;background:var(--yellow);border-radius:40px;color:#fff;padding:38px 67px;z-index:2}
.stats small{font-size:12px;display:block}
.stats h2{font-size:30px;font-weight:600;margin:6px 0 8px}
.stats p{font-size:10px}
.stats .tag{position:absolute;right:66px;top:61px;width:180px;height:40px;background:#fff;color:var(--ink);border-radius:20px;font-size:13px;font-weight:500;display:flex;align-items:center;justify-content:center}

/* about */
.band{left:0;width:1200px;background:var(--sky);border-radius:48px}
.about-title{left:134px;top:1186px;font-size:30px;font-weight:600;color:#fff}
.about-text{left:134px;top:1232px;width:345px;font-size:11.5px;line-height:19px;color:#fff}
.about-list{left:134px;top:1326px;list-style:none;color:#fff;font-size:12px;font-weight:600;line-height:19px}
.about-list li{display:flex;gap:6px;margin-bottom:6px}
.tick{flex:none;width:12px;height:12px;border-radius:50%;background:var(--yellow);margin-top:3px}

/* products */
.section-title{width:1200px;text-align:center;font-size:30px;font-weight:600}
.tabs{left:225px;top:1799px;display:flex;gap:8px}
.tab{height:40px;border-radius:20px;background:#eee;font-size:12px;font-weight:500;display:flex;align-items:center;justify-content:center}
.tab.is-active{background:var(--yellow);color:#fff}
.spec{left:574px;display:flex;gap:14px}
.num{flex:none;width:46px;height:46px;border-radius:50%;border:2px dashed var(--sky-soft);display:flex;align-items:center;justify-content:center}
.num span{width:36px;height:36px;border-radius:50%;background:var(--blue);color:#fff;font-size:13px;font-weight:600;display:flex;align-items:center;justify-content:center}
.num.sky span{background:var(--sky)}.num.yel span{background:var(--yellow)}.num.org span{background:#f2a72c}
.spec h4{font-size:15px;font-weight:600;margin-top:4px}
.spec p{font-size:11.5px;line-height:19px;color:var(--muted);width:340px}

/* news */
.news{top:2538px;width:290px}
.news .img{height:172px;border-radius:14px}
.news .date{margin-top:16px;padding-left:12px;font-size:12px;font-weight:600;color:#fff}
.news h4{padding-left:12px;font-size:15px;font-weight:600;color:#fff;margin-top:3px}
.news p{padding-left:12px;font-size:11.5px;line-height:19px;color:#eaf7fd}

/* contact */
.contact-row{left:222px;width:256px;display:flex;gap:22px;align-items:center;font-size:13px;padding:10px 0}
.contact-row.line{border-bottom:1px solid #d9dde3}
.social{top:3427px;width:34px;height:34px;border-radius:50%;background:var(--blue)}
.form-disc{left:556px;top:3078px;width:426px;height:426px;border-radius:50%;background:var(--yellow)}
.field{left:627px;width:282px;background:#fff;border-radius:8px;font-size:10px;color:#9aa0aa;padding:14px 24px}
.btn-send{left:628px;top:3373px;width:282px;height:38px;background:var(--blue);color:#fff;border-radius:19px;font-size:12px;font-weight:600;display:flex;align-items:center;justify-content:center}
.footer{left:0;top:3594px;width:1200px;height:47px;background:var(--footer);font-size:10px;display:flex;align-items:center;justify-content:center}
</style>
</head>
<body>

<div class="abs hero-bg"></div>

<header>
  <div class="abs logo site-logo"><span class="logo-dot"></span>Velmora DX</div>
  <nav class="abs nav">
    <span class="active">Home</span><span>About</span><span>Products</span><span>Science</span><span>Partners</span><span>Contact</span>
  </nav>
  <div class="abs btn-login">
    <svg width="14" height="14" viewBox="0 0 14 14"><rect x="6" y="1" width="7" height="12" rx="1" fill="none" stroke="#3b86d6" stroke-width="1.5"/><path d="M1 7h7M5 4l3 3-3 3" fill="none" stroke="#6cc7ee" stroke-width="1.5"/></svg>Login
  </div>
  <div class="abs btn-signup">Sign Up</div>
</header>

<section class="hero">
  <p class="abs eyebrow">Combining biomarker panels with</p>
  <h1 class="abs hero-title">Advanced analytics<br>for surveillance and early<br>detection of cancer</h1>
  <p class="abs hero-text">Non-invasive, urine-based diagnostics that prioritise precision and clinical actionability. Trusted scientific heritage, clinically validated performance.</p>
  <div class="abs btn-learn">Learn More</div>
  <p class="abs hero-link">For clinicians: Request onboarding</p>

  <div class="ph" style="left:652px;top:110px;width:450px;height:450px;background:var(--sky-soft)"></div>
  <div class="ph" role="img" aria-label="Scientist holding a flask in a laboratory" style="left:718px;top:185px;width:300px;height:310px;background:linear-gradient(135deg,#dfe9ef,#7fb0d6)"></div>
  <div class="ph" role="img" aria-label="Gloved hand holding a plant seedling" style="left:578px;top:110px;width:164px;height:164px;background:linear-gradient(135deg,#e8f0f4,#5f9dd6);border:4px solid #fff"></div>
  <div class="ph" role="img" aria-label="Researcher in lab cap and safety glasses" style="left:982px;top:208px;width:156px;height:176px;background:linear-gradient(135deg,#e6eef4,#9ac0df);border:4px solid #fff"></div>
  <div class="ph" role="img" aria-label="Microscope in a laboratory" style="left:648px;top:448px;width:138px;height:138px;background:linear-gradient(135deg,#c8d7e4,#3d5c7d);border:4px solid #fff"></div>
  <div class="abs pill" style="left:577px;top:289px;width:178px;height:46px;padding-left:16px">
    <svg width="38" height="22" viewBox="0 0 38 22"><path d="M2 10l9-7 8 5 8-5 9 7-9 9-8-5-8 5z" fill="#3b86d6"/></svg>Partner with us
  </div>
  <div class="abs pill" style="left:973px;top:423px;width:178px;height:72px;padding:0 12px;align-items:center">
    <svg width="30" height="32" viewBox="0 0 30 32"><path d="M2 2l26 14L2 30z" fill="#3b86d6"/></svg>
    <div><div style="font-size:12px;font-weight:600">Watch explainer</div><div style="font-size:8.5px;line-height:10px;color:var(--muted);font-weight:400">60-second overview<br>non invasive workflow<br>&amp; clinical impact.</div></div>
  </div>
</section>

<section class="features">
  <div class="abs feature" style="left:151px">
    <div class="f-icon"><svg width="34" height="34" viewBox="0 0 34 34"><circle cx="17" cy="17" r="13" fill="none" stroke="#f5c634" stroke-width="3"/><path d="M10 17l6 6 12-14" fill="none" stroke="#f5c634" stroke-width="3"/></svg></div>
    <h3>Non invasive</h3><p>Urine sample — painless and easy to collect.</p>
  </div>
  <div class="abs feature" style="left:379px">
    <div class="f-icon"><svg width="30" height="32" viewBox="0 0 30 32"><path d="M4 3h22l-8 12h-6zM15 15v12M6 29h18" fill="none" stroke="#f5c634" stroke-width="3"/></svg></div>
    <h3>Precision biomarkers</h3><p>Targeted biomarker panels developed from clinical cohorts.</p>
  </div>
  <div class="abs feature is-active" style="left:605px">
    <div class="f-icon"><svg width="34" height="34" viewBox="0 0 34 34"><rect x="8" y="8" width="18" height="18" rx="3" fill="#fff"/><path d="M12 3v5M17 3v5M22 3v5M12 26v5M17 26v5M22 26v5M3 12h5M3 17h5M3 22h5M26 12h5M26 17h5M26 22h5" stroke="#fff" stroke-width="2"/><text x="17" y="21" font-size="9" font-family="Poppins,sans-serif" font-weight="700" text-anchor="middle" fill="#f5c634">AI</text></svg></div>
    <h3>AI powered insights</h3><p>Advanced analytics for risk scoring &amp; interpretation.</p>
  </div>
  <div class="abs feature" style="left:834px">
    <div class="f-icon"><svg width="32" height="30" viewBox="0 0 32 30"><path d="M3 14L16 3l13 11v13H3z" fill="#f5c634"/><path d="M16 12v10M11 17h10" stroke="#3b86d6" stroke-width="3"/></svg></div>
    <h3>Clinically validated</h3><p>Spin out from AHUD and Harrowgate Cancer Institute.</p>
  </div>
</section>

<section class="stats abs">
  <small>Interim clinical performance</small>
  <h2>Sensitivity 86% · Specificity 90%</h2>
  <p>Retrospective validation on &gt;1,000 samples; ongoing prospective study. Actionable, clinic-ready outputs.</p>
  <div class="tag">UroGland (interim)</div>
</section>

<section class="about">
  <div class="abs band" style="top:1041px;height:589px"></div>
  <h2 class="abs about-title">About Us Velmora DX</h2>
  <p class="abs about-text">A Ashgrove Hollis University of Dunmere spin-out translating Harrowgate Cancer Institute research into clinic-ready, urine-based tests for early detection. Our mission is earlier detection, better outcomes.</p>
  <ul class="abs about-list">
    <li><span class="tick"></span>Mission &amp; vision.</li>
    <li><span class="tick"></span><span>Founding story (Ashgrove Hollis University<br>of Dunmere spin-out; Harrowgate Cancer Institute research)</span></li>
    <li><span class="tick"></span>Leadership bios (scientific &amp; commercial).</li>
    <li><span class="tick"></span>Advisors &amp; collaborators.</li>
    <li><span class="tick"></span>Timeline of company evolution.</li>
    <li><span class="tick"></span><span>Our name: Velmora Diagnostics<br>(bright star symbolism).</span></li>
  </ul>
  <div class="ph" role="img" aria-label="Researcher looking into a microscope" style="left:674px;top:1159px;width:390px;height:390px;background:linear-gradient(135deg,#eef1f3,#9fb7cc)"></div>
</section>

<section class="products">
  <h2 class="abs section-title" style="left:0;top:1700px">Products / Services</h2>
  <p class="abs" style="left:0;top:1758px;width:1200px;text-align:center;font-size:12px;color:var(--muted)"><b style="color:var(--ink);font-weight:500">GlandSURE™</b> (pancreatic cancer risk assessment &amp; surveillance).</p>
  <div class="abs tabs">
    <span class="tab is-active" style="width:141px">GlandSURE™</span>
    <span class="tab" style="width:140px">Technology</span>
    <span class="tab" style="width:231px">Science / Clinical Evidence</span>
    <span class="tab" style="width:216px">Partners &amp; Collaborations</span>
  </div>
  <div class="ph" role="img" aria-label="Gloved hand operating a laboratory analyser" style="left:191px;top:1905px;width:330px;height:330px;background:linear-gradient(135deg,#3c4fbf,#9ab4e8)"></div>
  <div class="ph" role="img" aria-label="Gloved hand holding a sample device over paperwork" style="left:170px;top:2098px;width:192px;height:192px;background:linear-gradient(135deg,#f2f3f6,#b9c6da);border:4px solid #fff"></div>

  <div class="abs spec" style="top:1945px"><div class="num"><span>01</span></div><div><h4>Indication</h4><p>high-risk individuals (familial history, pancreatitis, genetic risk).</p></div></div>
  <div class="abs spec" style="top:2017px"><div class="num sky"><span>02</span></div><div><h4>Clinical output</h4><p>Elevated vs Average risk.</p></div></div>
  <div class="abs spec" style="top:2085px"><div class="num yel"><span>03</span></div><div><h4>Development stage</h4><p>retrospective validation complete; prospective Uro-Gland study in progress; UK launch Q4 2025.</p></div></div>
  <div class="abs spec" style="top:2153px"><div class="num org"><span>04</span></div><div><h4>Target customers</h4><p>national health services, private hospitals, labs, pharma.</p></div></div>
  <p class="abs" style="left:573px;top:2229px;font-size:11.5px"><b style="font-weight:600">Pipeline</b>: future early cancer diagnostics, genetic predisposition, risk scores.</p>
</section>

<section class="news-section">
  <div class="abs band" style="top:2411px;height:460px"></div>
  <h2 class="abs section-title" style="left:0;top:2474px;color:#fff">News / Press / Blog</h2>
  <article class="abs news" style="left:150px">
    <div class="img" role="img" aria-label="Team reviewing a bar chart presentation" style="background:linear-gradient(135deg,#f1f1f1,#b7b0a8)"></div>
    <div class="date">▦ &nbsp;2025-07-12</div><h4>UroGland interim results presented</h4><p>Interim results show promising specificity and sensitivity in prospective cohort.</p>
  </article>
  <article class="abs news" style="left:455px">
    <div class="img" role="img" aria-label="Clinicians shaking hands at a partnership meeting" style="background:linear-gradient(135deg,#e7ecef,#8c9aa8)"></div>
    <div class="date">▦ &nbsp;2025-11-02</div><h4>Partnership with Harrowgate Health</h4><p>Clinical deployment pilot agreement signed for multi-site validation.</p>
  </article>
  <article class="abs news" style="left:760px">
    <div class="img" role="img" aria-label="Hand stamping a signed document" style="background:linear-gradient(135deg,#f3eeea,#d8b8a8)"></div>
    <div class="date">▦ &nbsp;2025-03-18</div><h4>New patent granted</h4><p>Patent granted covering diagnostic algorithm and biomarkers.</p>
  </article>
</section>

<section class="contact">
  <h2 class="abs section-title" style="left:0;top:2970px">Contact Us</h2>
  <p class="abs" style="left:0;top:3016px;width:1200px;text-align:center;font-size:12px;color:var(--muted)">For partnerships, clinical onboarding or investor enquiries, contact our team.</p>
  <div class="abs logo" style="left:226px;top:3122px;font-size:26px"><span class="logo-dot" style="width:38px;height:38px"></span>Velmora DX</div>
  <div class="abs contact-row line" style="top:3214px">
    <svg width="20" height="26" viewBox="0 0 20 26"><path d="M10 1a9 9 0 0 1 9 9c0 7-9 15-9 15S1 17 1 10a9 9 0 0 1 9-9z" fill="#f5c634"/><circle cx="10" cy="10" r="3" fill="#fff"/></svg>
    <span style="line-height:19px">48 Linden Crescent Suite 12,<br>Fairbrook, NY 10450</span>
  </div>
  <div class="abs contact-row line" style="top:3284px">
    <svg width="24" height="24" viewBox="0 0 24 24"><path d="M5 2l4 5-2 3c1 3 4 6 7 7l3-2 5 4-3 4C10 22 2 14 1 5z" fill="#f5c634"/></svg>
    <span>555-0142-881</span>
  </div>
  <div class="abs contact-row" style="top:3346px">
    <svg width="24" height="18" viewBox="0 0 24 18"><rect width="24" height="18" rx="2" fill="#f5c634"/><path d="M1 2l11 8 11-8" fill="none" stroke="#fff" stroke-width="2"/></svg>
    <span>hello@velmoradx.example</span>
  </div>
  <span class="abs social" style="left:230px" aria-label="Social profile"></span>
  <span class="abs social" style="left:273px" aria-label="Social profile"></span>
  <span class="abs social" style="left:315px" aria-label="Social profile"></span>

  <div class="abs form-disc"></div>
  <div class="abs field" style="top:3171px;height:44px">Enter your name</div>
  <div class="abs field" style="top:3223px;height:44px">Enter your email address</div>
  <div class="abs field" style="top:3276px;height:86px">Type your message</div>
  <div class="abs btn-send">Send message
    <svg style="position:absolute;right:14px" width="16" height="16" viewBox="0 0 16 16"><path d="M1 8l14-7-4 14-3-6z" fill="#f5c634"/></svg>
  </div>
</section>

<footer class="abs footer">Velmora © 2025. ALL RIGHTS RESERVED</footer>

</body>
</html>
```